Granite Ridge Holdings

I have a real estate investment business.

** I need editable vector files of the final design.

Industry/Entity Type

Real Estate

Contact Information for Business Card

I would like the card to be clear and direct with the company name and contact info. I would prefer not to have a design that is too busy (i.e., with excessive detail) in the business card.

Font styles to use
Sans Serif

Requirements
Must have
• My card must have the following information listed below:
• Company name: Grainite Ridge Holdings LLC
• My name: Daniel Vorsley
• Phone number: (555) 218-9067
• Email address: dtvorsley@mailbox-example.net
• Keywords: “Real Estate Investments”
Nice to have
• I would like to have a design that resembles the characteristics/uses of obsidian stone which resembles something related to strength and resilience. Perhaps something with sharp, sleek color transitions as well.

```html
<!DOCTYPE html>
<html lang="en">
<head>
<meta charset="utf-8">
<title>Grainite Ridge Holdings LLC – Business Card</title>
<link href="https://fonts.googleapis.com/css2?family=Inter:ital,wght@0,300;0,400;1,300&display=swap" rel="stylesheet">
<style>
  :root {
    --page-bg: #e9e9e8;
    --card-black: #040404;
    --ink-light: #f2f2f2;
    --ink-soft: #d8d8d8;
    --stone-dark: #2a2a2a;
    --stone-mid: #4c4c4c;
    --stone-light: #7a7a7a;
  }
  html, body {
    margin: 0;
    padding: 0;
    width: 1154px;
    height: 1200px;
    overflow: hidden;
    background: var(--page-bg);
    font-family: "Inter", "Helvetica Neue", Arial, sans-serif;
  }
  .card {
    position: absolute;
    left: 57px;
    top: 303px;
    width: 1040px;
    height: 594px;
    background: var(--card-black);
    overflow: hidden;
    box-shadow: 0 6px 18px rgba(0,0,0,0.25);
  }
  .company-name {
    position: absolute;
    left: 40px;
    top: 50px;
    margin: 0;
    font-weight: 300;
    font-size: 44px;
    line-height: 1.2;
    letter-spacing: -0.5px;
    color: var(--ink-light);
    white-space: nowrap;
  }
  .tagline {
    position: absolute;
    left: 42px;
    top: 112px;
    margin: 0;
    font-style: italic;
    font-weight: 300;
    font-size: 30px;
    line-height: 1.2;
    color: var(--ink-soft);
    white-space: nowrap;
  }
  .brand-square {
    position: absolute;
    left: 430px;
    top: 122px;
    width: 22px;
    height: 22px;
    box-sizing: border-box;
    border: 2px solid var(--ink-light);
  }
  .contact {
    position: absolute;
    left: 40px;
    top: 292px;
  }
  .contact-name {
    margin: 0 0 8px;
    font-weight: 400;
    font-size: 38px;
    line-height: 1.15;
    color: var(--ink-light);
  }
  .contact-line {
    margin: 0 0 6px;
    font-weight: 300;
    font-size: 22px;
    line-height: 1.3;
    color: var(--ink-soft);
  }
  .stone-photo {
    position: absolute;
    left: 0;
    bottom: 0;
    width: 100%;
    height: 190px;
    background: linear-gradient(to bottom, var(--card-black) 0%, var(--stone-dark) 35%, var(--stone-mid) 75%, var(--stone-light) 100%);
  }
</style>
</head>
<body>
  <section class="card">
    <h1 class="company-name">Grainite Ridge Holdings LLC</h1>
    <p class="tagline">Real Estate Investments</p>
    <span class="brand-square" aria-hidden="true"></span>

    <div class="contact">
      <p class="contact-name">Daniel Vorsley</p>
      <p class="contact-line">(555) 218-9067</p>
      <p class="contact-line">dtvorsley@mailbox-example.net</p>
    </div>

    <div class="stone-photo" role="img" aria-label="Photograph of a dark textured stone slab along the bottom of the card"></div>
  </section>
</body>
</html>
```